Kestwell Finanz AG needs web design

We need a website for a Swiss company: Kestwell Finanz AG. We offer our customers financial services such as advice and funds. We also have an interest rate calculator that we want to link to via a button on the website.

We are looking for a black and gold design. (Background: Black, Accents: Gold and White)
The design should convey security and growth. We have uploaded our logo in the attachment.
Font from the logo: Trajan Pro Regular

```html
<!DOCTYPE html>
<html lang="en">
<head>
<meta charset="utf-8">
<title>Kestwell Finanz AG</title>
<link href="https://fonts.googleapis.com/css2?family=Cinzel:wght@400;500&family=Roboto:wght@400;500&display=swap" rel="stylesheet">
<style>
:root{
  --black:#000;
  --panel:#0d0d0d;
  --card:#111;
  --gold:#b39a62;
  --gold-light:#cfb57a;
  --gold-dark:#8a7444;
  --white:#fff;
  --muted:#d8d8d8;
  --line:#3a3a3a;
}
*{box-sizing:border-box;margin:0;padding:0}
html,body{width:1200px;height:4062px;overflow:hidden;background:var(--black)}
body{position:relative;font-family:"Roboto",Arial,sans-serif;color:var(--white)}
.abs{position:absolute}
.serif{font-family:"Cinzel",Georgia,serif}
.section-title{position:absolute;left:0;width:1200px;text-align:center;font-family:"Cinzel",Georgia,serif;font-size:35px;letter-spacing:1px;font-weight:400}
.btn{position:absolute;background:var(--gold);color:var(--white);font-size:15px;font-weight:500;display:flex;align-items:center;justify-content:center;gap:8px;border-radius:3px}
.btn-dark{color:#111}

/* header */
.site-header{position:absolute;left:0;top:0;width:1200px;height:68px;background:var(--black);z-index:5}
.brand{position:absolute;left:112px;top:0;width:175px;height:98px;background:#050505;display:flex;align-items:center;justify-content:center;text-align:center;font-family:"Cinzel",Georgia,serif;color:var(--gold);font-size:15px;line-height:1.2;z-index:6}
.main-nav{position:absolute;left:326px;top:26px;display:flex;gap:28px;font-family:"Cinzel",Georgia,serif;font-size:14px}
.main-nav a{color:var(--white);text-decoration:none}
.main-nav .active{border-bottom:2px solid var(--gold);padding-bottom:6px}
.header-phone{position:absolute;left:802px;top:19px;display:flex;align-items:center;gap:10px;font-size:14px;font-weight:500}
.round-icon{width:30px;height:30px;border-radius:50%;background:var(--gold);display:flex;align-items:center;justify-content:center}

/* hero */
.hero{position:absolute;left:0;top:68px;width:1200px;height:657px;background:linear-gradient(110deg,#0a2a3f 0%,#113c5c 35%,#0b3350 60%,#061a2a 100%)}
.hero-panel{position:absolute;left:631px;top:137px;width:470px;height:306px;background:rgba(10,24,36,.6)}
.hero-panel h1{position:absolute;left:47px;top:50px;font-family:"Cinzel",Georgia,serif;font-weight:400;font-size:40px;line-height:66px;letter-spacing:1px}
.slide-arrow{position:absolute;top:272px;width:36px;height:36px;border-radius:50%;background:var(--white);display:flex;align-items:center;justify-content:center}

/* about */
.about-title{left:110px;top:805px;font-size:38px}
.about-text{left:110px;top:870px;width:480px;font-size:14.5px;line-height:25.8px;color:var(--muted)}

/* services */
.services{position:absolute;left:0;top:1301px;width:1200px;height:552px;background:linear-gradient(180deg,#121110,#0b0a09)}
.service-card{position:absolute;top:164px;width:284px;height:303px;background:var(--black);border:1px solid #2a2a2a;border-bottom:3px solid var(--gold);border-radius:14px 0 0 0;text-align:center}
.service-card.featured{background:linear-gradient(135deg,#c9af74,#9c8450);border-color:transparent;color:#222}
.service-icon{width:110px;height:110px;border-radius:50%;background:var(--gold);margin:28px auto 0;display:flex;align-items:center;justify-content:center}
.featured .service-icon{background:transparent;border:2px dashed #222}
.service-card h3{font-family:"Cinzel",Georgia,serif;font-weight:400;font-size:16px;margin-top:22px;letter-spacing:.5px}
.service-card p{font-size:15px;line-height:26px;color:var(--muted);margin-top:10px}
.featured p{color:#2b2b2b}
.read-more{display:inline-flex;align-items:center;gap:8px;margin-top:16px;font-size:14px;font-weight:500;color:var(--gold);text-decoration:underline}
.featured .read-more{color:#111}

/* testimonials */
.testimonial-text{left:200px;top:1993px;width:800px;text-align:center;font-size:14.5px;line-height:25.8px;color:var(--muted)}
.avatar{position:absolute;border-radius:50%;background:linear-gradient(160deg,#5a6b7d,#1f2a36);border:2px solid #999}

/* news */
.news{position:absolute;left:0;top:2361px;width:1200px;height:672px;background:linear-gradient(180deg,#101010,#0a0a0a)}
.news-card{position:absolute;width:478px;height:223px;background:var(--black)}
.news-photo{position:absolute;left:11px;top:8px;width:183px;height:207px}
.news-body{position:absolute;left:210px;top:26px;width:260px}
.news-body h3{font-family:"Cinzel",Georgia,serif;font-weight:400;font-size:15px;letter-spacing:.5px}
.news-meta{display:flex;gap:20px;font-size:14px;color:var(--gold);margin-top:11px}
.news-body p{font-size:14.5px;line-height:24.5px;color:var(--muted);margin-top:9px}
.news-link{display:flex;align-items:center;gap:8px;color:var(--gold);font-size:14px;font-weight:500;margin-top:10px}

/* contact form */
.field{position:absolute;border:1px solid #555;border-radius:3px;font-size:12px;color:var(--muted);display:flex;align-items:flex-start;gap:9px;padding:11px 16px}

/* footer */
.footer-brand{left:112px;top:3770px;width:200px;font-family:"Cinzel",Georgia,serif;font-size:20px;color:var(--gold);line-height:1.25}
.footer-heading{position:absolute;top:3756px;font-family:"Cinzel",Georgia,serif;font-size:16px;letter-spacing:.5px}
.footer-links{position:absolute;top:3794px;list-style:none;font-size:14.5px;line-height:34.5px;color:var(--muted)}
.footer-links li::before{content:"»";margin-right:9px;color:var(--white)}
.social{position:absolute;top:3933px;width:30px;height:30px;border:2px solid var(--white);border-radius:50%}
.contact-row{position:absolute;left:891px;display:flex;align-items:center;gap:15px;font-size:14.5px;color:var(--muted);line-height:24px}
.contact-ring{width:32px;height:32px;border:2px solid var(--white);border-radius:50%;display:flex;align-items:center;justify-content:center;flex-shrink:0}
</style>
</head>
<body>

<header class="site-header">
  <nav class="main-nav">
    <a class="active">HOME</a><a>ABOUT</a><a>SERVICES</a><a>BLOG</a><a>CONTACT US</a>
  </nav>
  <svg class="abs" style="left:755px;top:27px" width="16" height="16" viewBox="0 0 16 16"><circle cx="6.5" cy="6.5" r="4.5" fill="none" stroke="#fff" stroke-width="2"/><path d="M10 10l4.5 4.5" stroke="#fff" stroke-width="2.4"/></svg>
  <div class="header-phone">
    <span class="round-icon"><svg width="14" height="14" viewBox="0 0 24 24"><path fill="#fff" d="M6.6 10.8a15 15 0 006.6 6.6l2.2-2.2c.3-.3.7-.4 1-.2 1.1.4 2.3.6 3.6.6.6 0 1 .4 1 1V20c0 .6-.4 1-1 1A17 17 0 013 4c0-.6.4-1 1-1h3.5c.6 0 1 .4 1 1 0 1.3.2 2.5.6 3.6.1.3 0 .7-.2 1z"/></svg></span>
    +41 44 555 0182
  </div>
  <div class="btn" style="left:976px;top:13px;width:112px;height:41px">LOGIN
    <svg width="12" height="14" viewBox="0 0 12 14"><rect x="1" y="6" width="10" height="8" rx="1" fill="#fff"/><path d="M3 6V4a3 3 0 016 0v2" fill="none" stroke="#fff" stroke-width="2"/></svg>
  </div>
</header>
<div class="brand">KESTWELL<br>FINANZ AG</div>

<section class="hero" role="img" aria-label="Man holding a laptop in a server room with blue lights">
  <div class="hero-panel">
    <h1>WELCOME TO<br>KESTWELL FINANZ</h1>
    <div class="btn" style="left:47px;top:195px;width:248px;height:48px;font-size:14.5px">INTEREST RATE CALCULATOR</div>
  </div>
  <div class="slide-arrow" style="left:30px"><svg width="12" height="12" viewBox="0 0 12 12"><path d="M8 1L3 6l5 5" fill="none" stroke="#000" stroke-width="2.5"/></svg></div>
  <div class="slide-arrow" style="left:1125px"><svg width="12" height="12" viewBox="0 0 12 12"><path d="M4 1l5 5-5 5" fill="none" stroke="#000" stroke-width="2.5"/></svg></div>
</section>
<svg class="abs" style="left:0;top:565px" width="1200" height="162" viewBox="0 0 1200 162">
  <path d="M0 162 L0 150 C70 110 130 92 230 92 C400 94 530 60 596 22 C660 60 790 96 960 96 C1060 98 1140 120 1200 152 L1200 162 Z" fill="#000"/>
  <path d="M0 150 C70 110 130 92 230 92 C400 94 530 60 596 22 C660 60 790 96 960 96 C1060 98 1140 120 1200 152" fill="none" stroke="#b39a62" stroke-width="3"/>
</svg>

<h2 class="abs serif about-title" style="font-weight:400">ABOUT US</h2>
<p class="abs about-text">Lorem ipsum dolor sit amet, consectetur adipiscing elit, sed eiusmod tempor incididunt ut labore et dolore magna aliqua. Ut enim ad minim veniam, quis nostrud exercitation ullamco laboris nisi ut aliquip ex ea commodo consequat. Duis aute irure dolor in reprehenderit  voluptate velit esse cillum dolore eu fugiat nulla pariatur.Lorem ipsum dolor stit amet, consectetur adipiscing elit, sed do eiusmod tempor incididuntit labore et dolore magna aliqua.Ut enim ad minim veniam, quis nostrud exercitation ullamco laboris nisi ut aliquip ex ea commodo consequat Duis aute irure dolor in reprehenderit voluptate velit esse cillum doloe eu fugiat nulla pariatur enim ad minim  nulla veniam.</p>
<div class="btn" style="left:110px;top:1159px;width:150px;height:46px;font-size:14px">LEARN MORE
  <svg width="14" height="14" viewBox="0 0 14 14"><circle cx="7" cy="7" r="7" fill="#fff"/><path d="M5.5 4l3 3-3 3" fill="none" stroke="#b39a62" stroke-width="1.8"/></svg>
</div>
<div class="abs" style="left:684px;top:804px;width:408px;height:392px;border:1.5px solid var(--gold)"></div>
<div class="abs" role="img" aria-label="Two colleagues reviewing data on computer monitors in an office" style="left:658px;top:823px;width:404px;height:390px;background:linear-gradient(135deg,#3e5468,#1c2a38 55%,#4a5a6a)"></div>

<section class="services">
  <h2 class="section-title" style="top:74px">OUR SERVICES</h2>
  <div class="service-card" style="left:140px">
    <div class="service-icon"><svg width="56" height="50" viewBox="0 0 56 50"><rect x="4" y="30" width="8" height="18" fill="#111"/><rect x="16" y="22" width="8" height="26" fill="#111"/><rect x="28" y="26" width="8" height="22" fill="#111"/><rect x="40" y="14" width="8" height="34" fill="#111"/><path d="M4 22L18 10l12 8L50 2" fill="none" stroke="#111" stroke-width="3"/></svg></div>
    <h3>LOREM IPSUM DOLOR SIT</h3>
    <p>Lorem ipsum dolor consectetur<br>adipiscing elit sed do eiusmod.</p>
    <span class="read-more">READ MORE <svg width="15" height="15" viewBox="0 0 14 14"><circle cx="7" cy="7" r="7" fill="#b39a62"/><path d="M5.5 4l3 3-3 3" fill="none" stroke="#000" stroke-width="1.8"/></svg></span>
  </div>
  <div class="service-card featured" style="left:458px">
    <div class="service-icon"><svg width="56" height="56" viewBox="0 0 56 56"><rect x="10" y="8" width="26" height="36" fill="none" stroke="#111" stroke-width="2.5"/><rect x="15" y="24" width="4" height="12" fill="#111"/><rect x="22" y="18" width="4" height="18" fill="#111"/><circle cx="36" cy="34" r="9" fill="none" stroke="#111" stroke-width="2.5"/><path d="M42 40l8 8" stroke="#111" stroke-width="3"/></svg></div>
    <h3>LOREM IPSUM DOLOR SIT</h3>
    <p>Lorem ipsum dolor consectetur<br>adipiscing elit sed do eiusmod.</p>
    <span class="read-more">READ MORE <svg width="15" height="15" viewBox="0 0 14 14"><circle cx="7" cy="7" r="7" fill="#111"/><path d="M5.5 4l3 3-3 3" fill="none" stroke="#c9af74" stroke-width="1.8"/></svg></span>
  </div>
  <div class="service-card" style="left:776px">
    <div class="service-icon"><svg width="58" height="50" viewBox="0 0 58 50"><circle cx="29" cy="10" r="6" fill="#111"/><circle cx="14" cy="14" r="5" fill="#111"/><circle cx="44" cy="14" r="5" fill="#111"/><path d="M6 40l14-10h18l14 10-10 6H16z" fill="#111"/></svg></div>
    <h3>LOREM IPSUM DOLOR SIT</h3>
    <p>Lorem ipsum dolor consectetur<br>adipiscing elit sed do eiusmod.</p>
    <span class="read-more">READ MORE <svg width="15" height="15" viewBox="0 0 14 14"><circle cx="7" cy="7" r="7" fill="#b39a62"/><path d="M5.5 4l3 3-3 3" fill="none" stroke="#000" stroke-width="1.8"/></svg></span>
  </div>
</section>

<h2 class="section-title" style="top:1932px">OUR TESTIMONIALS</h2>
<p class="abs testimonial-text">Lorem ipsum dolor sit amet, consectetur adipiscing elit, sed do eiusmod tempor incididunt ut labore et dolore magna aliqenim  minim veniam,quis nostrud exercitation ullamco laboris nisi aliquip commodo consequat. Duis aute irure dolor in reprehenderit in voluptate velit esse cillum dolore eu fugiat nulla pariatur. Excepteur sint occaecat cupidatat non proident, sunt in culpa qui officia deserunt mollit anim id est voluptate velit esse cillum dolore eu fugiat nulla pariatur laborum velit esse cillum dolore eu fugiat nulla pariatur.</p>
<div class="avatar" role="img" aria-label="Client portrait" style="left:469px;top:2160px;width:60px;height:60px"></div>
<div class="avatar" role="img" aria-label="Client portrait" style="left:554px;top:2145px;width:92px;height:92px;border-color:#ccc"></div>
<div class="avatar" role="img" aria-label="Client portrait" style="left:671px;top:2160px;width:60px;height:60px"></div>
<div class="abs" style="left:0;top:2262px;width:1200px;text-align:center;font-size:14px;font-weight:500;color:var(--gold)">LENA MARBACH</div>

<section class="news">
  <h2 class="section-title" style="top:54px">LATEST NEWS</h2>
  <article class="news-card" style="left:112px;top:146px">
    <div class="news-photo" role="img" aria-label="Hands signing financial documents with a pen" style="background:linear-gradient(135deg,#e8ecef,#b8c2cc)"></div>
    <div class="news-body"><h3>LOREM IPSUM DOLOR SIT</h3><div class="news-meta"><span>Comments</span><span>2022/03/9</span></div><p>Lorem ipsum consectetur adipiscing sed eiusmod tempor et incididunt ut labore et dolore magna enim adimn.</p><span class="news-link">LEARN MORE <svg width="14" height="14" viewBox="0 0 14 14"><circle cx="7" cy="7" r="7" fill="#b39a62"/><path d="M5.5 4l3 3-3 3" fill="none" stroke="#000" stroke-width="1.8"/></svg></span></div>
  </article>
  <article class="news-card" style="left:609px;top:146px">
    <div class="news-photo" role="img" aria-label="Calculator on printed financial charts" style="background:linear-gradient(135deg,#d8dde2,#7e8a96)"></div>
    <div class="news-body"><h3>LOREM IPSUM DOLOR SIT</h3><div class="news-meta"><span>Comments</span><span>2022/03/9</span></div><p>Lorem ipsum consectetur adipiscing sed eiusmod tempor et incididunt ut labore et dolore magna enim adimn.</p><span class="news-link">LEARN MORE <svg width="14" height="14" viewBox="0 0 14 14"><circle cx="7" cy="7" r="7" fill="#b39a62"/><path d="M5.5 4l3 3-3 3" fill="none" stroke="#000" stroke-width="1.8"/></svg></span></div>
  </article>
  <article class="news-card" style="left:112px;top:386px">
    <div class="news-photo" role="img" aria-label="Technician with tablet in a data centre aisle" style="background:linear-gradient(135deg,#2c3a46,#6b7884)"></div>
    <div class="news-body"><h3>LOREM IPSUM DOLOR SIT</h3><div class="news-meta"><span>Comments</span><span>2022/03/9</span></div><p>Lorem ipsum consectetur adipiscing sed eiusmod tempor et incididunt ut labore et dolore magna enim adimn.</p><span class="news-link">LEARN MORE <svg width="14" height="14" viewBox="0 0 14 14"><circle cx="7" cy="7" r="7" fill="#b39a62"/><path d="M5.5 4l3 3-3 3" fill="none" stroke="#000" stroke-width="1.8"/></svg></span></div>
  </article>
  <article class="news-card" style="left:609px;top:386px">
    <div class="news-photo" role="img" aria-label="Analyst working at several monitors" style="background:linear-gradient(135deg,#1d3a52,#0c1a26)"></div>
    <div class="news-body"><h3>LOREM IPSUM DOLOR SIT</h3><div class="news-meta"><span>Comments</span><span>2022/03/9</span></div><p>Lorem ipsum consectetur adipiscing sed eiusmod tempor et incididunt ut labore et dolore magna enim adimn.</p><span class="news-link">LEARN MORE <svg width="14" height="14" viewBox="0 0 14 14"><circle cx="7" cy="7" r="7" fill="#b39a62"/><path d="M5.5 4l3 3-3 3" fill="none" stroke="#000" stroke-width="1.8"/></svg></span></div>
  </article>
</section>

<h2 class="section-title" style="top:3110px">GRT IN TOUCH</h2>
<div class="field" style="left:248px;top:3190px;width:348px;height:39px">&#9679; First Name</div>
<div class="field" style="left:606px;top:3190px;width:346px;height:39px">&#9679; Last Name</div>
<div class="field" style="left:248px;top:3242px;width:348px;height:39px">&#9993; Email</div>
<div class="field" style="left:606px;top:3242px;width:346px;height:39px">&#9647; Phone</div>
<div class="field" style="left:248px;top:3293px;width:704px;height:133px">&#9679; Comments</div>
<div class="btn btn-dark" style="left:541px;top:3468px;width:120px;height:44px;font-size:14px">SUBMIT
  <svg width="13" height="12" viewBox="0 0 13 12"><path d="M0 5L13 0 10 12 6 8z" fill="#111"/></svg>
</div>

<svg class="abs" style="left:0;top:3540px" width="1200" height="170" viewBox="0 0 1200 170">
  <path d="M0 12 C90 60 200 76 330 80 C470 86 560 120 600 166 C640 120 730 86 870 80 C1000 76 1110 60 1200 12" fill="none" stroke="#b39a62" stroke-width="3"/>
</svg>

<div class="abs footer-brand">KESTWELL<br>FINANZ AG</div>
<div class="abs serif" style="left:112px;top:3892px;font-size:16px">FOLLOW US</div>
<div class="social" style="left:112px" aria-label="Social profile"></div>
<div class="social" style="left:152px" aria-label="Social profile"></div>
<div class="social" style="left:192px" aria-label="Social profile"></div>
<div class="social" style="left:232px" aria-label="Social profile"></div>

<div class="footer-heading" style="left:427px">QUICKLINKS</div>
<ul class="footer-links" style="left:427px"><li>Home</li><li>About</li><li>Services</li><li>Blog</li><li>Contact Us</li></ul>
<div class="footer-heading" style="left:658px">OTHERLINKS</div>
<ul class="footer-links" style="left:658px"><li>Contact Us</li><li>FAQ</li><li>Services</li><li>Privacy</li><li>Policy</li></ul>
<div class="footer-heading" style="left:891px">CONTACT US</div>
<div class="contact-row" style="top:3800px"><span class="contact-ring"><svg width="14" height="14" viewBox="0 0 24 24"><path fill="#fff" d="M6.6 10.8a15 15 0 006.6 6.6l2.2-2.2c.3-.3.7-.4 1-.2 1.1.4 2.3.6 3.6.6.6 0 1 .4 1 1V20c0 .6-.4 1-1 1A17 17 0 013 4c0-.6.4-1 1-1h3.5c.6 0 1 .4 1 1 0 1.3.2 2.5.6 3.6.1.3 0 .7-.2 1z"/></svg></span>+41 44 555 0182</div>
<div class="contact-row" style="top:3861px"><span class="contact-ring"><svg width="14" height="11" viewBox="0 0 14 11"><rect x="1" y="1" width="12" height="9" fill="none" stroke="#fff" stroke-width="1.5"/><path d="M1 1l6 5 6-5" fill="none" stroke="#fff" stroke-width="1.5"/></svg></span>info@kestwellfinanz.ch</div>
<div class="contact-row" style="top:3920px"><span class="contact-ring"><svg width="12" height="15" viewBox="0 0 12 15"><path d="M6 14S1 8.5 1 5.5a5 5 0 0110 0C11 8.5 6 14 6 14z" fill="none" stroke="#fff" stroke-width="1.5"/><circle cx="6" cy="5.5" r="1.7" fill="#fff"/></svg></span>125,Lorem ipsumt amet<br>consectetur adipiscing</div>

<div class="abs" style="left:112px;top:4006px;width:976px;height:1px;background:var(--line)"></div>
<div class="abs" style="left:0;top:4024px;width:1200px;text-align:center;font-size:13px;color:var(--muted)">© 2022 Copyrights Kestwell Finanz  All Rights Reserved.</div>

</body>
</html>
```